Landing page for Cloud Kitchen buisnies

We need a landing page design fully functional for our Cloud Kitchen company wich is based in Dubai we have a industrial kitchen setup up from where we operate our own online food brands wich are only availble for delivery

Target Market(s)

Its just a company Profile

Requirements
Must have
• Company name is Saffron Lane Group. We have the Logo already

LOGO AND DOMAIN WE HAVE
Nice to have
• Proffesionel high quality design

```html
<!DOCTYPE html>
<html lang="en">
<head>
<meta charset="utf-8">
<title>Saffron Lane Group — Delivery-only kitchens</title>
<link href="https://fonts.googleapis.com/css2?family=Open+Sans:wght@400;600&display=swap" rel="stylesheet">
<style>
  :root {
    --gold: #f5b82e;
    --yellow: #f6bf2a;
    --white: #ffffff;
    --ink: #1c1c1c;
    --body: #333333;
    --dark: #2e2e2e;
    --partners-bg: #f4f4f4;
    --panel: rgba(70, 70, 70, 0.9);
  }
  * { box-sizing: border-box; margin: 0; padding: 0; }
  html, body { width: 1200px; height: 3514px; overflow: hidden; }
  body { font-family: "Open Sans", Arial, sans-serif; color: var(--body); background: var(--white); position: relative; }
  section, header, footer { position: absolute; left: 0; width: 1200px; }

  /* brand name used where the logo stands */
  .brand { position: absolute; display: flex; align-items: center; gap: 10px; color: var(--gold); font-weight: 600; letter-spacing: 1px; }
  .brand-dot { width: 14px; height: 14px; border-radius: 50%; background: var(--gold); flex: none; }

  /* hero */
  .hero { top: 0; height: 464px; background: linear-gradient(180deg, #1b1a18 0%, #2b2722 45%, #15130f 100%); }
  .hero-photo { position: absolute; inset: 0; background: radial-gradient(ellipse at 50% 40%, rgba(120,100,80,0.35), rgba(0,0,0,0) 60%); }
  .hero .brand { left: 30px; top: 48px; font-size: 20px; }
  .nav { position: absolute; right: 56px; top: 51px; display: flex; gap: 23px; }
  .nav a { color: var(--gold); text-decoration: none; font-size: 16px; font-weight: 600; }
  .hero-kicker { position: absolute; top: 226px; width: 100%; text-align: center; color: var(--white); font-size: 32px; }
  .hero-title { position: absolute; top: 266px; width: 100%; text-align: center; color: var(--gold); font-size: 45px; line-height: 51px; font-weight: 600; }

  /* about */
  .about { top: 464px; height: 736px; }
  .about-photo { position: absolute; left: 175px; width: 404px; height: 270px; }
  .about-photo.plates { top: 96px; background: linear-gradient(135deg, #f2f0ee 0%, #ddd6cc 50%, #b88a55 100%); }
  .about-photo.oven { top: 366px; background: linear-gradient(135deg, #2a2320 0%, #7a3b22 50%, #d0603a 80%, #3a3450 100%); }
  .about-text { position: absolute; left: 608px; top: 114px; width: 420px; }
  .eyebrow { color: var(--gold); font-size: 21px; }
  .about-title { color: var(--ink); font-size: 27px; line-height: 32px; font-weight: 400; margin-top: 24px; }
  .about-text p { font-size: 15.5px; line-height: 21px; margin-top: 20px; }
  .about-text p.lead { color: var(--ink); margin-top: 24px; }

  /* services */
  .services { top: 1200px; height: 633px; background: var(--yellow); color: var(--white); text-align: center; }
  .services-title { position: absolute; top: 51px; width: 100%; font-size: 33px; font-weight: 600; }
  .services-sub { position: absolute; top: 108px; width: 100%; font-size: 15.5px; line-height: 21px; }
  .service { position: absolute; top: 199px; width: 300px; }
  .service svg { display: block; margin: 0 auto; }
  .service-label { margin-top: 34px; font-size: 21px; line-height: 25px; font-weight: 600; }

  /* cook */
  .cook { top: 1833px; height: 710px; background: linear-gradient(160deg, #5a5a5a 0%, #3a3a3a 45%, #242424 100%); text-align: right; color: var(--white); }
  .cook .brand { right: 74px; top: 135px; font-size: 24px; }
  .cook-title { position: absolute; right: 74px; top: 250px; color: var(--gold); font-size: 64px; line-height: 76px; font-weight: 600; }
  .cook-lead { position: absolute; right: 74px; top: 426px; width: 640px; font-size: 27px; line-height: 32px; font-weight: 600; }
  .cook-note { position: absolute; right: 74px; top: 570px; width: 680px; font-size: 21px; line-height: 26px; }

  /* partners */
  .partners { top: 2543px; height: 627px; background: var(--partners-bg); }
  .partners-title { position: absolute; left: 106px; top: 72px; color: var(--ink); font-size: 41px; font-weight: 400; }
  .partner-grid { position: absolute; left: 106px; top: 182px; display: grid; grid-template-columns: repeat(5, 175px); grid-auto-rows: 175px; column-gap: 28.5px; row-gap: 7px; }
  .partner { background: var(--white); display: flex; align-items: center; justify-content: center; }
  .partner.dark { background: #111; }
  .partner.tile-pattern { background: linear-gradient(135deg, #2b1a1a, #4a2a1e 50%, #1f2a22); }
  .partner.blue-pattern { background: linear-gradient(135deg, #2f7fc4, #e9eef5 50%, #2f7fc4); }
  .badge { border-radius: 50%; }

  /* footer */
  .contact { top: 3170px; height: 344px; background: linear-gradient(180deg, #d9dbdd 0%, #eceded 60%, #f3f3f3 100%); }
  .contact-panel { position: absolute; left: 569px; top: 51px; width: 571px; height: 236px; background: var(--panel); color: var(--white); }
  .contact-kicker { position: absolute; left: 57px; top: 57px; font-size: 21px; }
  .contact-title { position: absolute; left: 57px; top: 85px; color: var(--gold); font-size: 28px; font-weight: 600; }
  .contact-lines { position: absolute; left: 57px; top: 135px; font-size: 15.5px; line-height: 21px; }
  .contact .brand { left: 310px; top: 110px; font-size: 21px; }
</style>
</head>
<body>

<header class="hero">
  <div class="hero-photo" role="img" aria-label="Chef at work in a dimly lit professional kitchen"></div>
  <div class="brand"><span class="brand-dot"></span>SAFFRON LANE GROUP</div>
  <nav class="nav">
    <a href="#about">About Us</a>
    <a href="#services">Services</a>
    <a href="#kitchens">Our Kitchens</a>
    <a href="#partners">Our Partners</a>
    <a href="#contact">Contact</a>
  </nav>
  <p class="hero-kicker">Delivery-only kitchens</p>
  <h1 class="hero-title">Grow your restaurant business with<br>lower risk and higher return</h1>
</header>

<section class="about" id="about">
  <div class="about-photo plates" role="img" aria-label="Plated dishes on a white platter"></div>
  <div class="about-photo oven" role="img" aria-label="Baked dish being taken out of an oven"></div>
  <div class="about-text">
    <p class="eyebrow">ABOUT SAFFRON LANE</p>
    <h2 class="about-title">WE ARE DUBAI-BASED<br>CLOUD KITCHEN</h2>
    <p class="lead">We have branch in Dubai Tech Park, which will allow us to cater to 30 new locations in the Emirate, including Arabian Ranches, Barsha South, Studio City, Sports City, and more.</p>
    <p>Our team will work around the clock to support your growing roster of clients. Ensuring to help retain your revenue generation amid this critical phase.</p>
    <p>We also brought forward the need for intensified health and safety measures that Saffron Lane is mobilizing in collaboration with local authorities.</p>
    <p>We also provide additional services that include a call center and full delivery service fleet giving your brand the opportunity to achieve maximum access and market reach to your customer base.</p>
  </div>
</section>

<section class="services" id="services">
  <h2 class="services-title">Our Services</h2>
  <p class="services-sub">We provide a range of services that include a state of the art kitchen facility,<br>Call Center and Food Delivery Operations.</p>

  <div class="service" style="left:125px">
    <svg width="230" height="262" viewBox="0 0 230 262">
      <polygon points="115,0 230,65 230,197 115,262 0,197 0,65" fill="#fff"/>
      <rect x="50" y="70" width="130" height="120" rx="10" fill="#fbe3a0" role="img" aria-label="Kitchen equipment icon"/>
    </svg>
    <p class="service-label">Premium Kitchen<br>Facility</p>
  </div>
  <div class="service" style="left:450px">
    <svg width="230" height="262" viewBox="0 0 230 262">
      <polygon points="115,0 230,65 230,197 115,262 0,197 0,65" fill="#fff"/>
      <rect x="50" y="70" width="130" height="120" rx="10" fill="#fbe3a0" role="img" aria-label="Call center headset icon"/>
    </svg>
    <p class="service-label">Call Center<br>Service</p>
  </div>
  <div class="service" style="left:776px">
    <svg width="230" height="262" viewBox="0 0 230 262">
      <polygon points="115,0 230,65 230,197 115,262 0,197 0,65" fill="#fff"/>
      <rect x="50" y="70" width="130" height="120" rx="10" fill="#fbe3a0" role="img" aria-label="Delivery rider on a scooter icon"/>
    </svg>
    <p class="service-label">Integrated<br>Food Delivery</p>
  </div>
</section>

<section class="cook" id="kitchens" role="img" aria-label="Stainless steel kitchen workstation with bowls and trays">
  <div class="brand"><span class="brand-dot"></span>SAFFRON LANE GROUP</div>
  <h2 class="cook-title">ALL YOU HAVE<br>TO DO IS COOK</h2>
  <p class="cook-lead">Our kitchen equipped with complete tools for cooking your food. So you could serve the best food for your customers</p>
  <p class="cook-note">All the tools provided are for one purpose, boosting your revenue while we taking care most of the bussiness process for you</p>
</section>

<section class="partners" id="partners">
  <h2 class="partners-title">OUR PARTNERS</h2>
  <div class="partner-grid">
    <div class="partner" role="img" aria-label="Partner brand badge"><div class="badge" style="width:70px;height:70px;background:#7cc242"></div></div>
    <div class="partner" role="img" aria-label="Partner brand badge"><div class="badge" style="width:130px;height:130px;background:#8cc63f"></div></div>
    <div class="partner blue-pattern" role="img" aria-label="Partner brand badge"><div style="width:120px;height:70px;background:#fff"></div></div>
    <div class="partner" role="img" aria-label="Partner brand badge"><div class="badge" style="width:60px;height:60px;background:#9cc43a"></div></div>
    <div class="partner" role="img" aria-label="Partner brand badge"><div style="width:110px;height:30px;background:#8a2a22"></div></div>
    <div class="partner" role="img" aria-label="Partner brand badge"><div style="width:70px;height:70px;background:#e03a3a"></div></div>
    <div class="partner dark" role="img" aria-label="Partner brand badge"><div class="badge" style="width:150px;height:150px;border:3px solid #e0533d"></div></div>
    <div class="partner tile-pattern" role="img" aria-label="Partner brand badge"><div style="width:100px;height:80px;border:1px solid #ddd"></div></div>
    <div class="partner" role="img" aria-label="Partner brand badge"><div class="badge" style="width:150px;height:150px;background:#d6232a"></div></div>
    <div class="partner" role="img" aria-label="Partner brand badge"><div class="badge" style="width:160px;height:160px;background:#6a5a4c"></div></div>
  </div>
</section>

<footer class="contact" id="contact" role="img" aria-label="Hazy skyline of Dubai towers">
  <div class="contact-panel">
    <p class="contact-kicker">For inquiry</p>
    <h2 class="contact-title">CONTACT US</h2>
    <p class="contact-lines">+971 40 555 0182<br>info@saffronlanegroup.com</p>
    <div class="brand"><span class="brand-dot"></span>SAFFRON LANE GROUP</div>
  </div>
</footer>

</body>
</html>
```